Stainless Steel Letter Box plate

I need to have a letter box plate front in stainless steel that I what to have designed.

I have attached the Design of the brick letter box that has already been made.

The dimensions of the brick are set and the hole for the letters is in a set location. ( Give or take small amount )

The stainless steel manufacturer has sent a draft of the front of the plate that I thought was a bit boring and plain ( Attached )

The Stainless plate is to go on the front of the Letter box and wrap around to the left side. Brick and render will be ( is to be ) shown on the top and bottom margins of the stainless steel plate

Remember it needs to be cut out of Stainless Steel so that the number 4 needs to have joins.

The Stainless will go on the Front of the letter box and wrap around the left hand side of the letter box.

Industry/Entity Type

Steel

Requirements
Must have
• Letter Drop needs to be in set location
• Number 4
• Mirov or Mirov Rd

```html
<!DOCTYPE html>
<html lang="en">
<head>
<meta charset="utf-8">
<title>Letter Box Plate Concepts</title>
<link rel="stylesheet" href="https://fonts.googleapis.com/css2?family=Alfa+Slab+One&family=Black+Ops+One&family=Comfortaa:wght@300&family=Poiret+One&family=Josefin+Sans:wght@700&family=Aldrich&family=Michroma&family=Julius+Sans+One&family=Russo+One&family=Bungee&family=Alegreya+Sans+SC:wght@800&family=Stardos+Stencil:wght@700&family=Graduate&family=Share+Tech+Mono&display=swap">
<style>
:root{
  --page:#ffffff;
  --ink:#1c1c1c;
  --steel-light:#f4f4f4;
  --steel-mid:#cfcfcf;
  --steel-dark:#a9a9a9;
  --label:#c4c4c4;
  --outline:#6e6e6e;
}
html,body{margin:0;padding:0;overflow:hidden}
body{width:1200px;height:899px;background:var(--page);position:relative;font-family:sans-serif}
.option-label{position:absolute;font-family:"Share Tech Mono",monospace;font-size:17px;color:var(--label);letter-spacing:4px}
.plate{position:absolute;width:426px;height:118px;overflow:hidden;
  background:
    radial-gradient(ellipse 60% 90% at 72% 0%,rgba(255,255,255,.95),rgba(255,255,255,0) 70%),
    linear-gradient(100deg,var(--steel-dark) 0%,var(--steel-mid) 30%,var(--steel-light) 55%,var(--steel-mid) 80%,var(--steel-dark) 100%);}
.letter-slot{position:absolute;left:19px;top:19px;width:110px;height:17px;background:var(--ink);box-shadow:1px 1px 0 #fff}
.street{position:absolute;left:18px;bottom:14px;color:var(--ink);font-size:24px;line-height:1;white-space:nowrap;text-shadow:1px 1px 0 #fff}
.house-no{position:absolute;left:250px;top:12px;width:80px;text-align:center;font-size:88px;line-height:1;color:var(--ink);text-shadow:2px 2px 0 #fff}
.hollow{color:#e2e2e2;-webkit-text-stroke:1.5px var(--ink);text-shadow:2px 2px 0 var(--outline)}
</style>
</head>
<body>
<span class="option-label" style="left:68px;top:80px">1</span>
<div class="plate" style="left:119px;top:68px"><div class="letter-slot"></div>
  <span class="street" style="font-family:'Graduate',serif;font-size:20px;letter-spacing:2px">MIROV RD</span>
  <span class="house-no" style="font-family:'Alfa Slab One',serif">4</span></div>

<span class="option-label" style="left:657px;top:80px">2</span>
<div class="plate" style="left:708px;top:68px"><div class="letter-slot"></div>
  <span class="street hollow" style="font-family:'Comfortaa',sans-serif;font-weight:300;font-size:27px;-webkit-text-stroke:1px var(--outline);text-shadow:none">Mirov</span>
  <span class="house-no hollow" style="font-family:'Poiret One',sans-serif;left:240px">4</span></div>

<span class="option-label" style="left:68px;top:240px">3</span>
<div class="plate" style="left:119px;top:230px"><div class="letter-slot"></div>
  <span class="street hollow" style="font-family:'Poiret One',sans-serif;font-size:30px;letter-spacing:2px;-webkit-text-stroke:1px var(--outline);text-shadow:none">Mirov Rd</span>
  <span class="house-no hollow" style="font-family:'Poiret One',sans-serif;left:245px">4</span></div>

<span class="option-label" style="left:657px;top:240px">4</span>
<div class="plate" style="left:708px;top:232px"><div class="letter-slot"></div>
  <span class="street" style="font-family:'Alegreya Sans SC',sans-serif;font-weight:800;font-size:28px">Mirov</span>
  <span class="house-no" style="font-family:'Black Ops One',sans-serif;left:225px">4</span></div>

<span class="option-label" style="left:68px;top:402px">5</span>
<div class="plate" style="left:119px;top:392px"><div class="letter-slot"></div>
  <span class="street" style="font-family:'Alfa Slab One',serif;font-size:23px">Mirov Rd</span>
  <span class="house-no" style="font-family:'Stardos Stencil',sans-serif;font-weight:700;left:235px;font-size:96px;top:6px">4</span></div>

<span class="option-label" style="left:657px;top:402px">6</span>
<div class="plate" style="left:708px;top:392px"><div class="letter-slot"></div>
  <span class="street" style="font-family:'Josefin Sans',sans-serif;font-weight:700;font-size:28px">Mirov</span>
  <span class="house-no hollow" style="font-family:'Poiret One',sans-serif;left:245px">4</span></div>

<span class="option-label" style="left:68px;top:562px">7</span>
<div class="plate" style="left:119px;top:554px"><div class="letter-slot"></div>
  <span class="street" style="font-family:'Aldrich',sans-serif;font-size:25px">Mirov Rd</span>
  <span class="house-no hollow" style="font-family:'Aldrich',sans-serif;left:248px">4</span></div>

<span class="option-label" style="left:657px;top:562px">8</span>
<div class="plate" style="left:708px;top:554px"><div class="letter-slot"></div>
  <span class="street" style="font-family:'Michroma',sans-serif;font-size:21px">Mirov</span>
  <span class="house-no" style="font-family:'Michroma',sans-serif;left:245px;font-size:80px;top:16px;text-shadow:-3px -2px 0 var(--outline)">4</span></div>

<span class="option-label" style="left:68px;top:722px">9</span>
<div class="plate" style="left:119px;top:714px"><div class="letter-slot"></div>
  <span class="street hollow" style="font-family:'Julius Sans One',sans-serif;font-size:26px;-webkit-text-stroke:1px var(--ink)">MIROV RD</span>
  <span class="house-no" style="font-family:'Poiret One',sans-serif;left:255px;font-size:92px;top:10px">4</span></div>

<span class="option-label" style="left:657px;top:722px">10</span>
<div class="plate" style="left:708px;top:714px"><div class="letter-slot"></div>
  <span class="street" style="font-family:'Russo One',sans-serif;font-size:20px;letter-spacing:1px">MIROV</span>
  <span class="house-no" style="font-family:'Bungee',sans-serif;left:240px;font-size:84px;top:10px">4</span></div>
</body>
</html>
```